Brevolt Solar business cards for carl dunwiddie

Need a solar business card designed. I sell solar systems to home owners. Company’s name is Brevolt solar. I want the business card to have this.
Brevolt Solar
Carl Dunwiddie
210.555.0143
Solar consultant
Cdunwiddie@brevoltsolar.example
I would like the card to be black and green with the brevolt logo on it if possible. If it’s possible to make atleast one of the designs green background with black lettering I would like to see that.
No upfront cost! Start saving today!
Target Market(s)
Residential home owners
Industry/Entity Type
Solar Energy
Contact Information for Business Card
Brevolt Solar
Carl Dunwiddie
210.555.0143
Solar consultant
Cdunwiddie@brevoltsolar.example
Also if it would look better by adding in one of these that would be fine.

```html
<!DOCTYPE html>
<html lang="en">
<head>
<meta charset="utf-8">
<title>Brevolt Solar business cards</title>
<link rel="stylesheet" href="https://fonts.googleapis.com/css2?family=Lato:wght@400;700&display=swap">
<style>
  :root {
    --page: #efe9dc;
    --card-dark: #262626;
    --card-green: #70bf45;
    --ink: #1f1f1f;
    --white: #ffffff;
    --accent-green: #74c043;
    --shadow: 0 18px 30px rgba(0,0,0,0.28);
  }
  * { margin: 0; padding: 0; box-sizing: border-box; }
  html, body { width: 1200px; height: 901px; overflow: hidden; }
  body {
    background: var(--page);
    font-family: "Lato", sans-serif;
    position: relative;
  }
  .card {
    position: absolute;
    width: 620px;
    height: 354px;
    box-shadow: var(--shadow);
    overflow: hidden;
  }

  /* Back of card */
  .card-back {
    left: 80px; top: 70px;
    background: var(--card-dark);
  }
  .card-back .brand {
    position: absolute;
    left: 0; right: 0; top: 130px;
    text-align: center;
    color: var(--white);
    font-weight: 700;
    font-size: 34px;
    letter-spacing: 1px;
  }
  .card-back .brand .brand-mark {
    display: inline-block;
    width: 14px; height: 14px;
    background: var(--white);
    margin-right: 10px;
    vertical-align: 4px;
  }
  .card-back .web-rule {
    position: absolute;
    left: 0; right: 0; bottom: 58px;
    display: flex;
    align-items: center;
    gap: 12px;
    color: var(--accent-green);
    font-size: 12px;
    letter-spacing: 0.5px;
  }
  .card-back .web-rule::before,
  .card-back .web-rule::after {
    content: "";
    flex: 1;
    height: 1px;
    background: var(--accent-green);
  }

  /* Front of card */
  .card-front {
    left: 500px; top: 470px;
    background: var(--card-green);
  }
  .card-front .brand {
    position: absolute;
    left: 42px; top: 40px;
    color: var(--white);
    font-weight: 700;
    font-size: 30px;
    letter-spacing: 0.5px;
  }
  .card-front .brand .brand-mark {
    display: inline-block;
    width: 12px; height: 12px;
    background: var(--white);
    margin-right: 8px;
    vertical-align: 4px;
  }
  .card-front .holder {
    position: absolute;
    left: 42px; top: 150px;
    color: var(--ink);
  }
  .holder .name {
    font-size: 30px;
    font-weight: 400;
    letter-spacing: 0.3px;
  }
  .card-front .name-rule {
    position: absolute;
    left: 42px; right: 70px; top: 194px;
    height: 2px;
    background: var(--ink);
  }
  .card-front .details {
    position: absolute;
    left: 60px; top: 204px;
    color: var(--ink);
    font-size: 14px;
    line-height: 1.45;
  }
  .details .role { font-size: 15px; }
  .details .company-rule {
    width: 22px; height: 1px; background: var(--ink);
    margin: 4px 0 2px -14px;
  }
  .details .contact {
    display: flex; align-items: center; gap: 8px;
    margin-top: 4px;
    color: var(--white);
  }
  .details .contact svg { width: 16px; height: 16px; }
  .card-front .base-band {
    position: absolute;
    left: 0; right: 0; bottom: 0;
    height: 18px;
    background: var(--card-dark);
  }
  .card-front .band-tab {
    position: absolute;
    right: 0; top: 170px;
    width: 42px; height: 184px;
    background: var(--card-dark);
  }
  .card-front .band-tab::before {
    content: "";
    position: absolute;
    left: 8px; top: 6px;
    width: 8px; height: 14px;
    background: var(--white);
  }
</style>
</head>
<body>

  <section class="card card-back" aria-label="Card back">
    <div class="brand"><span class="brand-mark"></span>Brevolt Solar</div>
    <div class="web-rule">www.brevoltsolar.example</div>
  </section>

  <section class="card card-front" aria-label="Card front">
    <div class="band-tab"></div>
    <div class="base-band"></div>
    <div class="brand"><span class="brand-mark"></span>Brevolt Solar</div>
    <div class="holder"><p class="name">Carl Dunwiddie</p></div>
    <div class="name-rule"></div>
    <div class="details">
      <p class="role">Solar consultant</p>
      <div class="company-rule"></div>
      <p class="company">Brevolt Solar</p>
      <p class="contact">
        <svg viewBox="0 0 16 16" aria-hidden="true"><circle cx="8" cy="8" r="7" fill="none" stroke="#fff" stroke-width="1.3"/><path d="M5.5 4.5l1.4 1.6-.8 1.1c.5 1 1.2 1.7 2.2 2.2l1.1-.8 1.6 1.4-.9 1.2c-2.8-.5-4.9-2.6-5.4-5.4z" fill="#fff"/></svg>
        210.555.0143
      </p>
      <p class="contact">
        <svg viewBox="0 0 16 16" aria-hidden="true"><rect x="1.5" y="3.5" width="13" height="9" fill="none" stroke="#fff" stroke-width="1.2"/><path d="M1.5 3.5l6.5 5 6.5-5" fill="none" stroke="#fff" stroke-width="1.2"/></svg>
        Cdunwiddie@brevoltsolar.example
      </p>
    </div>
  </section>

</body>
</html>
```